Pactwise - Training I Consulting I Review - Related to Contracts/Agreements

We provide legal services, we need a plattform to book video online trainings or local trainings classes and appointments (with calendar feature to select date and see availability at screen), payment over internet, legal document creation over webpage, videos will be produces in the next 3 - 4 moths so this is a place holder item. Participants for the Online trainings shall have a login in area with secured password. Appointments for local trainings and Consulting. Consider Outline in file attached. I can send you also a video with more explanation regarding the purpose.

Target Market(s)

Startup/scale up Software companies that intent to have an international business and need help with their contracts, to sell their products. Sales persons.

Industry/Entity Type

Legal

Coding

Coded - Design and coding required

Number of Pages Required

5+ page

Font styles to use
Serif
Sans Serif

Colors
000000
eeeeee
f5f5f5
ffffff
f8fcfd
3277b5
ecf7fb
cadf82
86cfc6

Requirements
Must have
• See file pactwise attached with outline. Moreover see here first starting point: https://moritz-ebbing.sitebuildr-demo.net/mysite-1 . Main inspiration comes from www.advisoryhub-demo.net from the log in area, see the outline in the file attached with the screen shots. At the end I need someone who can draft the full webpage and maintain it for a yearly fee. It must be simple and well structured layout. Lean. 1st landing page shall not scroll, 2 landing page only a little to see the testimonials and foster of page. There should be a Progress Bar to indicate the booking/selection process. Calendar booking. Easy fast booking.
• I like the colour mix, the feeling and the easy structor of:
• https://www.artpitch-demo.net/design/6374387or
• https://www.artpitch-demo.net/design/6372391 or https://www.artpitch-demo.net/design/6374366
• https://www.agencyfind-demo.net/en/web-design/belgium-be
• https://www.artpitch-demo.net/design/5896857
• https://www.artpitch-demo.net/design/5902173
• https://www.artpitch-demo.net/design/17197349
• https://www.artpitch-demo.net/design/5464461
• https://www.artpitch-demo.net/design/7180908
Nice to have
• page for evaluation and interview, see outline attached in the file with screen shots. Document upload.
Should not have
• many pictures, long scroll down pages on the 1st and 2nd ladding pages, many colours and forms. No need for news letter, search field, no need for links to Chatterly and other social media (except workNet).

```html
<!DOCTYPE html>
<html lang="en">
<head>
<meta charset="utf-8">
<title>Pactwise – Services</title>
<link rel="stylesheet" href="https://fonts.googleapis.com/css2?family=Lora:wght@400;700&family=Open+Sans:wght@400;600;700&display=swap">
<style>
:root{
  --red:#e8232a;
  --green:#cadf82;
  --sky:#cbe3f1;
  --dark-card:#434240;
  --text:#333333;
  --muted:#555555;
  --white:#ffffff;
  --line-blue:#3277b5;
  --serif:'Lora', Georgia, serif;
  --sans:'Open Sans', Arial, sans-serif;
}
*{box-sizing:border-box;margin:0;padding:0}
html,body{width:1200px;height:1172px;overflow:hidden;background:var(--white);font-family:var(--sans);color:var(--text)}
.page{position:relative;width:1200px;height:1172px}

.hero{position:absolute;left:0;top:0;width:1200px;height:359px;
  background:linear-gradient(100deg,#3b3633 0%,#5a534d 30%,#6b6a68 55%,#4a4b4f 80%,#3a3b3e 100%);
  border-bottom:1px solid var(--line-blue)}
.hero-shade{position:absolute;inset:0;background:rgba(20,20,20,.35)}
.brand{position:absolute;left:115px;top:22px;font-family:var(--serif);font-size:36px;color:var(--white);letter-spacing:1px}
.nav{position:absolute;top:38px;left:637px;font-size:13.5px;color:var(--white)}
.nav a{color:inherit;text-decoration:none;position:absolute;white-space:nowrap;top:0}
.nav .active{color:var(--red);font-weight:600}
.login{position:absolute;left:999px;top:31px;width:88px;height:31px;background:var(--red);color:var(--white);
  font-weight:700;font-size:13.5px;display:flex;align-items:center;justify-content:center;border-radius:2px;letter-spacing:.5px}
.hero-title{position:absolute;top:166px;width:100%;text-align:center;font-family:var(--serif);font-weight:400;font-size:50px;color:var(--white);letter-spacing:1px}

.service{position:absolute;top:333px;width:313px;height:324px;text-align:center;box-shadow:0 2px 6px rgba(0,0,0,.12)}
.service::before{content:"";position:absolute;left:0;top:0;width:100%;height:7px;background:var(--accent)}
.service.light{background:var(--white);color:var(--text)}
.service.dark{background:var(--dark-card);color:var(--white)}
.service h2{position:absolute;top:32px;width:100%;font-family:var(--serif);font-weight:400;font-size:16px;letter-spacing:.5px}
.service svg.icon{position:absolute;top:71px;left:124px;width:64px;height:64px}
.service p{position:absolute;top:161px;left:20px;right:20px;font-size:13.5px;line-height:21.7px}
.cta-label{position:absolute;top:236px;width:100%;font-family:var(--serif);font-weight:700;font-size:12px;color:var(--accent);letter-spacing:.3px}
.diamond{position:absolute;top:268px;left:143px;width:27px;height:27px;background:var(--accent);transform:rotate(45deg);border-radius:2px}
.diamond span{position:absolute;inset:0;display:flex;align-items:center;justify-content:center;transform:rotate(-45deg);font-size:16px;line-height:1}

.section-title{position:absolute;top:690px;width:100%;text-align:center;font-family:var(--serif);font-weight:700;font-size:23px;color:#444;letter-spacing:.5px}

.testimonial{position:absolute;top:752px;width:313px;height:241px;background:var(--white);box-shadow:0 1px 6px rgba(0,0,0,.1)}
.avatar{position:absolute;left:22px;top:28px;width:67px;height:67px;border-radius:50%;background:radial-gradient(circle at 50% 45%,#c99a7e,#6b4a3a)}
.stars{position:absolute;left:109px;top:50px;display:flex;gap:15px}
.stars svg{width:17px;height:17px}
.testimonial p{position:absolute;left:111px;top:84px;width:188px;font-size:13px;line-height:21.7px;color:var(--muted);text-align:justify;text-align-last:left}
.testimonial .name{position:absolute;left:111px;top:181px;font-weight:700;font-size:15px;color:#444}

.footer-links{position:absolute;top:1069px;width:100%;text-align:center;font-size:15px;color:#444}
.footer-links span{margin:0 9px}
.copyright{position:absolute;top:1126px;width:100%;text-align:center;font-size:13px;color:#444}
.page-mark{position:absolute;left:1130px;top:1116px;font-size:13px;color:#444}
</style>
</head>
<body>
<div class="page">
  <header class="hero" role="img" aria-label="Photo of smiling business team in an office">
    <div class="hero-shade"></div>
  </header>
  <div class="brand">Pactwise</div>
  <nav class="nav">
    <a style="left:0">Refere Someone</a>
    <a class="active" style="left:135px">Services</a>
    <a style="left:220px">Partner</a>
    <a style="left:295px">Contact</a>
  </nav>
  <div class="login">LOGIN</div>
  <h1 class="hero-title">SERVICES</h1>

  <section class="service light" style="left:112px;--accent:var(--red)">
    <h2>CONTRACT TRAINING</h2>
    <svg class="icon" viewBox="0 0 64 64" fill="none" stroke="#666" stroke-width="1.6">
      <rect x="2" y="2" width="46" height="34"/><line x1="0" y1="38" x2="38" y2="38"/>
      <circle cx="12" cy="14" r="4"/><line x1="20" y1="12" x2="40" y2="12"/><line x1="20" y1="18" x2="34" y2="18"/>
      <rect x="8" y="24" width="12" height="8"/><line x1="24" y1="28" x2="36" y2="28"/>
      <circle cx="47" cy="40" r="7"/><path d="M34 62v-6c0-5 6-8 13-8s13 3 13 8v6z"/><line x1="36" y1="46" x2="28" y2="36"/>
    </svg>
    <p>I'm a paragraph. Click here to add your own text and edit me. It’s easy. Just click “Edit Text” or double click me.</p>
    <div class="cta-label">BOOK</div>
    <div class="diamond"><span style="color:#fff">+</span></div>
  </section>

  <section class="service dark" style="left:444px;--accent:var(--green)">
    <h2>CONTRACT CONSULTING</h2>
    <svg class="icon" viewBox="0 0 64 64" fill="none" stroke="#fff" stroke-width="1.8">
      <circle cx="32" cy="20" r="12"/><path d="M18 22v-4a14 14 0 0 1 28 0v4"/>
      <rect x="14" y="17" width="5" height="10" rx="2"/><rect x="45" y="17" width="5" height="10" rx="2"/>
      <path d="M47 27c0 5-6 7-12 7"/><path d="M6 62v-8c0-8 10-13 26-13s26 5 26 13v8z"/>
      <path d="M26 41l6 8 6-8"/><line x1="32" y1="49" x2="32" y2="62"/>
    </svg>
    <p>Massa euismod sollicitudin. Pellentesque suscipit enim tempor turpis donec. Et quis dolor. Purus lobortis diam.</p>
    <div class="cta-label">APPOINTMENT</div>
    <div class="diamond"><span style="color:#444">+</span></div>
  </section>

  <section class="service dark" style="left:776px;--accent:var(--sky)">
    <h2>CONTRACT REVIEW</h2>
    <svg class="icon" viewBox="0 0 64 64" fill="none" stroke="#fff" stroke-width="1.8">
      <rect x="10" y="22" width="9" height="20"/><path d="M19 24l8-10V4c5 0 7 4 6 12h14a4 4 0 0 1 0 8 4 4 0 0 1 0 8 4 4 0 0 1-2 8H19"/>
      <path d="M8 48l2.5 5 5.5 .8-4 3.8 1 5.4-5-2.6-5 2.6 1-5.4-4-3.8 5.5-.8z"/>
      <path d="M32 48l2.5 5 5.5 .8-4 3.8 1 5.4-5-2.6-5 2.6 1-5.4-4-3.8 5.5-.8z"/>
      <path d="M56 48l2.5 5 5.5 .8-4 3.8 1 5.4-5-2.6-5 2.6 1-5.4-4-3.8 5.5-.8z"/>
    </svg>
    <p>Massa euismod sollicitudin. Pellentesque suscipit enim tempor turpis donec. Et quis dolor. Purus lobortis diam.</p>
    <div class="cta-label">REQUEST</div>
    <div class="diamond"><span style="color:#444">+</span></div>
  </section>

  <h2 class="section-title">TESTIMONIALS</h2>

  <svg width="0" height="0" style="position:absolute">
    <defs>
      <path id="star" d="M12 2l2.9 6.6 7.1.6-5.4 4.7 1.6 7L12 17.3 5.8 21l1.6-7L2 9.2l7.1-.6z"/>
    </defs>
  </svg>

  <article class="testimonial" style="left:112px">
    <div class="avatar" role="img" aria-label="Portrait photo of client"></div>
    <div class="stars">
      <svg viewBox="0 0 24 24"><use href="#star" fill="#e8232a"/></svg>
      <svg viewBox="0 0 24 24"><use href="#star" fill="#e8232a"/></svg>
      <svg viewBox="0 0 24 24"><use href="#star" fill="#e8232a"/></svg>
      <svg viewBox="0 0 24 24"><use href="#star" fill="none" stroke="#e8232a" stroke-width="2"/></svg>
      <svg viewBox="0 0 24 24"><use href="#star" fill="none" stroke="#e8232a" stroke-width="2"/></svg>
    </div>
    <p>Massa euismod sollicitudin. Pellentesque suscipit enim tempor turpis donec. Et quis dolor. Purus lobortis diam.</p>
    <div class="name">Nora Velic</div>
  </article>

  <article class="testimonial" style="left:444px">
    <div class="avatar" role="img" aria-label="Portrait photo of client" style="background:radial-gradient(circle at 50% 45%,#c9a38a,#4a3a30)"></div>
    <div class="stars">
      <svg viewBox="0 0 24 24"><use href="#star" fill="#e8232a"/></svg>
      <svg viewBox="0 0 24 24"><use href="#star" fill="#e8232a"/></svg>
      <svg viewBox="0 0 24 24"><use href="#star" fill="#e8232a"/></svg>
      <svg viewBox="0 0 24 24"><use href="#star" fill="none" stroke="#e8232a" stroke-width="2"/></svg>
      <svg viewBox="0 0 24 24"><use href="#star" fill="none" stroke="#e8232a" stroke-width="2"/></svg>
    </div>
    <p>Massa euismod sollicitudin. Pellentesque suscipit enim tempor turpis donec. Et quis dolor. Purus lobortis diam.</p>
    <div class="name">Elias</div>
  </article>

  <article class="testimonial" style="left:776px">
    <div class="avatar" role="img" aria-label="Portrait photo of client" style="background:radial-gradient(circle at 50% 45%,#6b4a38,#e9e9e9 90%)"></div>
    <div class="stars">
      <svg viewBox="0 0 24 24"><use href="#star" fill="#e8232a"/></svg>
      <svg viewBox="0 0 24 24"><use href="#star" fill="#e8232a"/></svg>
      <svg viewBox="0 0 24 24"><use href="#star" fill="#e8232a"/></svg>
      <svg viewBox="0 0 24 24"><use href="#star" fill="none" stroke="#e8232a" stroke-width="2"/></svg>
      <svg viewBox="0 0 24 24"><use href="#star" fill="none" stroke="#e8232a" stroke-width="2"/></svg>
    </div>
    <p>Massa euismod sollicitudin. Pellentesque suscipit enim tempor turpis donec. Et quis dolor. Purus lobortis diam.</p>
    <div class="name">Tomas Reid</div>
  </article>

  <footer>
    <div class="footer-links">Evaluation<span>/</span>Students<span>/</span>Policies<span>/</span>Team<span>/</span>Market Feedback<span>/</span>Templates<span>/</span>Tools<span>/</span>Contact</div>
    <div class="copyright">©2018 Pactwise.com</div>
    <div class="page-mark">M1</div>
  </footer>
</div>
</body>
</html>
```